Tovrelan Ltda

Logo design focused on: - Construction of civil works - Electrical services - Metal structures - Equipment rental Tomás Ibarra Leiva Manager tovrelan.ltda@brevomail.example 56 9 48215037 Quelitoco s / n, Sorimar, Valle de Orvencia

Building

Colors
33a6d7
0292cd
33b8a4
0555a3

```html
<!DOCTYPE html>
<html lang="es">
<head>
<meta charset="utf-8">
<title>Tovrelan Ltda – Tarjeta de presentación</title>
<link rel="stylesheet" href="https://fonts.googleapis.com/css2?family=Montserrat:wght@400;500;600&display=swap">
<style>
  :root {
    --sky: #33a6d7;
    --azure: #0292cd;
    --teal: #33b8a4;
    --navy: #0555a3;
    --card-blue: #0f74bd;
    --stripe: #12aebd;
    --white: #ffffff;
    --backdrop: #e9ecef;
  }
  * { margin: 0; padding: 0; box-sizing: border-box; }
  html, body {
    width: 1200px; height: 837px; overflow: hidden;
    background: var(--backdrop);
    font-family: "Montserrat", Arial, sans-serif;
  }
  .business-card {
    position: absolute; left: 100px; top: 132px;
    width: 1000px; height: 572px;
    border-radius: 34px; overflow: hidden;
    background: var(--white);
    box-shadow: 0 10px 30px rgba(0,0,0,.18);
  }
  .card-art { position: absolute; inset: 0; }
  .brand {
    position: absolute; left: 268px; top: 38px;
    display: flex; align-items: center; gap: 18px;
  }
  .brand-dot {
    width: 84px; height: 84px; border-radius: 50%;
    background: var(--azure);
  }
  .brand-name {
    font-size: 42px; font-weight: 500; color: var(--navy);
    letter-spacing: 1px;
  }
  .holder { position: absolute; left: 70px; top: 262px; color: var(--white); }
  .holder-name { font-size: 40px; font-weight: 600; letter-spacing: .5px; }
  .holder-role { font-size: 20px; font-weight: 400; margin-top: 2px; }
  .contact {
    position: absolute; left: 572px; top: 418px;
    color: var(--white); font-size: 18px; line-height: 1.4;
    white-space: nowrap;
  }
  .contact-row { display: flex; align-items: center; gap: 10px; }
  .contact-row svg { width: 16px; height: 16px; flex: none; }
  .contact-address { margin-top: 16px; }
</style>
</head>
<body>
  <main class="business-card">
    <svg class="card-art" viewBox="0 0 1000 572" aria-hidden="true">
      <path d="M0,150 C240,140 440,250 620,300 C800,350 900,390 1000,452 L1000,572 L0,572 Z" fill="var(--card-blue)"/>
      <path d="M0,118 C240,108 440,218 620,268 C800,318 900,358 1000,420" fill="none" stroke="var(--stripe)" stroke-width="11"/>
      <path d="M0,98 C240,88 440,198 620,248 C800,298 900,338 1000,400" fill="none" stroke="var(--stripe)" stroke-width="5"/>
      <line x1="546" y1="334" x2="478" y2="478" stroke="var(--white)" stroke-width="2"/>
    </svg>

    <div class="brand">
      <span class="brand-dot"></span>
      <span class="brand-name">Tovrelan Ltda</span>
    </div>

    <div class="holder">
      <p class="holder-name">Tomás Ibarra Leiva</p>
      <p class="holder-role">Gerente</p>
    </div>

    <div class="contact">
      <p class="contact-row">
        <svg viewBox="0 0 18 18"><rect x="1" y="4" width="16" height="11" rx="1" fill="var(--white)"/><path d="M1,4 L9,11 L17,4" fill="none" stroke="var(--card-blue)" stroke-width="1.5"/></svg>
        tovrelan.ltda@brevomail.example
      </p>
      <p class="contact-row">
        <svg viewBox="0 0 18 18"><path d="M4,2 L7,2 L8,6 L6,7.5 C7,10 8,11 10.5,12 L12,10 L16,11 L16,14 C16,15 15,16 14,16 C8,16 2,10 2,4 C2,3 3,2 4,2 Z" fill="var(--white)"/></svg>
        +56 9 48215037
      </p>
      <p class="contact-address">Quelitoco s/n, Sorimar,<br>Valle de Orvencia</p>
    </div>
  </main>
</body>
</html>
```